Verdane Kiwi Root Essence Prime Serum - Product Label

Hi Guys,

I threw up a rough label sketch. Looking to keep the label clean and fresh.

LABEL DIMENSIONS: 4.05 in (Height) x 1.18 in (Diameter)

Industry/Entity Type

Beauty Aid

Font styles to use
Serif

Colors
0255a3
0592cd
6b449b
ffc214

Requirements
Must have
• Lumivelle
• __________
• S K I N
Nice to have
• We can try purple, gold and black or stick with the blue scheme we have going.

```html
<!DOCTYPE html>
<html lang="en">
<head>
<meta charset="utf-8">
<title>Verdane Kiwi Root Essence Prime Serum – Label</title>
<link rel="stylesheet" href="https://fonts.googleapis.com/css2?family=Cormorant+Garamond:wght@300;500;600&family=Lora:wght@400;600&display=swap">
<style>
  :root {
    --backdrop: #cfd3d9;
    --label: #fbfbfc;
    --ink: #1e1e24;
    --ink-soft: #34343a;
    --navy: #0255a3;
    --sky: #0592cd;
    --violet: #6b449b;
    --gold: #ffc214;
  }
  * { margin: 0; padding: 0; box-sizing: border-box; }
  html, body { width: 1200px; height: 1200px; overflow: hidden; }
  body {
    background: radial-gradient(circle at 50% 45%, #e7e9ec 0%, var(--backdrop) 100%);
    font-family: "Lora", Georgia, serif;
    color: var(--ink);
    position: relative;
  }
  .label {
    position: absolute;
    left: 50px; top: 347px;
    width: 1100px; height: 505px;
    background: var(--label);
    box-shadow: 0 18px 40px rgba(60, 64, 72, 0.28);
  }
  .mark-dot {
    position: absolute;
    width: 26px; height: 26px;
    border-radius: 50%;
    background: var(--sky);
  }
  .mark-dot.left { left: 135px; top: 50px; }
  .mark-dot.right { left: 937px; top: 50px; }

  .info-column { position: absolute; left: 33px; width: 257px; top: 100px; }
  .section-title {
    background: var(--violet);
    color: #fff;
    font-family: "Lora", Georgia, serif;
    font-weight: 400;
    font-size: 15px;
    line-height: 22px;
    padding-left: 9px;
    margin-bottom: 7px;
  }
  .section-body {
    font-size: 13px;
    line-height: 18px;
    text-align: justify;
    padding: 0 6px 0 9px;
    color: var(--ink-soft);
    margin-bottom: 24px;
  }

  .brand-block { position: absolute; left: 330px; width: 440px; top: 38px; text-align: center; }
  .brand-dot {
    width: 50px; height: 50px; border-radius: 50%;
    background: var(--sky);
    margin: 0 auto 16px;
  }
  .brand-name {
    font-family: "Cormorant Garamond", Georgia, serif;
    font-weight: 300;
    font-size: 62px;
    line-height: 62px;
    letter-spacing: 6px;
    text-transform: uppercase;
    color: var(--navy);
  }
  .brand-tag {
    font-family: "Cormorant Garamond", Georgia, serif;
    font-weight: 600;
    font-size: 16px;
    letter-spacing: 10px;
    color: var(--violet);
    margin-top: 8px;
    padding-left: 10px;
  }
  .brand-rule {
    width: 90px; height: 2px;
    background: var(--gold);
    margin: 10px auto 0;
  }
  .product-name {
    font-family: "Cormorant Garamond", Georgia, serif;
    font-weight: 600;
    font-size: 33px;
    line-height: 38px;
    margin-top: 24px;
    color: var(--ink);
  }
  .product-type {
    width: 366px;
    margin: 12px auto 0;
    background: var(--violet);
    color: #fff;
    font-family: "Lora", Georgia, serif;
    font-size: 23px;
    line-height: 36px;
    letter-spacing: 3px;
  }
  .net-content {
    margin-top: 30px;
    font-family: "Lora", Georgia, serif;
    font-weight: 600;
    font-size: 19px;
    color: var(--navy);
  }

  .side-column { position: absolute; left: 835px; top: 140px; width: 230px; }
  .distributor { font-size: 13px; line-height: 19px; color: var(--ink-soft); }
  .distributor strong { color: var(--navy); font-weight: 600; }
  .badges { display: flex; justify-content: space-between; align-items: center; margin-top: 40px; padding-right: 10px; }
  .side-rule { height: 2px; background: var(--gold); margin-top: 44px; }
  .side-band {
    margin-top: 14px;
    height: 110px;
    background: linear-gradient(135deg, var(--navy), var(--sky));
  }
</style>
</head>
<body>
  <main class="label" aria-label="Product label">
    <span class="mark-dot left"></span>
    <span class="mark-dot right"></span>

    <section class="info-column">
      <h2 class="section-title">Ingredients</h2>
      <p class="section-body">Purified Water, (VerdaCell Stem Cell) Malus Domestica, Glycerin, Lecithin, Phenoxyethanol Collagen, Palmitoyl Tetrapeptide-3, (Peptixel 3000), Propylene Glycol, Polyglutamic Acid, Phoenoxyethanol, Hydroethylcellulose, Propylene Glycol, Benzylalcohol, Dehydroacetic Acid</p>
      <h2 class="section-title">How to use</h2>
      <p class="section-body">Wash area where you will apply the Verdane Kiwi Root Essence Serum thoroughly. Apply the product and let absorb for 15 minutes the apply moisturizer if desire.</p>
    </section>

    <section class="brand-block">
      <div class="brand-dot"></div>
      <h1 class="brand-name">Lumivelle</h1>
      <p class="brand-tag">S K I N</p>
      <div class="brand-rule"></div>
      <p class="product-name">VERDANE KIWI ROOT<br>ESSENCE PRIME</p>
      <p class="product-type">SERUM</p>
      <p class="net-content">1 fl. oz / 30 ml</p>
    </section>

    <section class="side-column">
      <div class="distributor">
        <p>Distributed by <strong>LUMIVELLE</strong></p>
        <p>Address:</p>
        <p>Website:</p>
      </div>
      <div class="badges">
        <svg width="44" height="44" viewBox="0 0 44 44" aria-hidden="true"><rect x="5" y="5" width="34" height="34" rx="7" fill="none" stroke="var(--violet)" stroke-width="3"/></svg>
        <svg width="44" height="44" viewBox="0 0 44 44" aria-hidden="true"><rect x="6" y="10" width="32" height="26" rx="3" fill="none" stroke="var(--ink)" stroke-width="2.5"/></svg>
        <svg width="52" height="52" viewBox="0 0 52 52" aria-hidden="true"><circle cx="26" cy="26" r="23" fill="var(--gold)"/></svg>
      </div>
      <div class="side-rule"></div>
      <div class="side-band" role="img" aria-label="Product code area"></div>
    </section>
  </main>
</body>
</html>
```